All-Natural Head Lice Removal company

I need a business card with my pre-existing logo. We are a new company located in Portland Oregon that goes into peoples homes to help with head lice removal. My products and approach are all- natural and also will be around children.On my current logo we used Teal Bl and the color Green. I am open to new ideas just want it simple and creative

Target Market(s)

my biggest market is families of school aged children

Industry/Entity Type

Business

Contact Information for Business Card

see upload for details from previous business card

Font styles to use
Serif

Colors
33a6d7
9bcb3b
f37122

Requirements
Must have
• Basic information/ logo put into a creative format that is catching to the eye
Nice to have
• creative

```html
<!DOCTYPE html>
<html lang="en">
<head>
<meta charset="utf-8">
<title>Bright Comb Business Card</title>
<link href="https://fonts.googleapis.com/css2?family=Arvo:wght@400;700&display=swap" rel="stylesheet">
<style>
  :root {
    --page: #e9ebed;
    --sky-light: #7fd3f3;
    --sky: #33a6d7;
    --sky-deep: #1f86c8;
    --ink: #222326;
    --ink-soft: #2e3034;
    --leaf: #9bcb3b;
    --white: #ffffff;
  }
  * { margin: 0; padding: 0; box-sizing: border-box; }
  html, body {
    width: 1200px; height: 913px; overflow: hidden;
    background: var(--page);
    font-family: "Arvo", serif;
  }
  .canvas { position: relative; width: 1200px; height: 913px; }

  .card {
    position: absolute;
    width: 540px; height: 308px;
    border-radius: 16px;
    overflow: hidden;
    background: linear-gradient(160deg, var(--sky-light) 0%, var(--sky) 55%, var(--sky-deep) 100%);
    box-shadow: 0 10px 24px rgba(0,0,0,.18);
  }
  .card--front { left: 60px; top: 110px; }
  .card--back { left: 600px; top: 495px; }

  .wave { position: absolute; inset: 0; }

  .brand {
    position: absolute;
    display: flex; align-items: center; gap: 10px;
  }
  .brand__dot { border-radius: 50%; background: var(--leaf); flex: none; }
  .brand__name { font-weight: 700; color: var(--ink); white-space: nowrap; }

  .card--front .brand { left: 34px; top: 118px; }
  .card--front .brand__dot { width: 34px; height: 34px; }
  .card--front .brand__name { font-size: 32px; }

  .identity {
    position: absolute; right: 30px; top: 26px; text-align: right;
  }
  .identity__name { color: var(--leaf); font-size: 19px; letter-spacing: 1px; text-transform: uppercase; }
  .identity__role { color: var(--white); font-size: 11px; letter-spacing: 1px; text-transform: uppercase; margin-top: 4px; }
  .identity__service { color: var(--ink-soft); font-size: 13px; margin-top: 6px; }

  .contacts {
    position: absolute; right: 24px; top: 130px; list-style: none; text-align: right;
  }
  .contacts li {
    display: flex; justify-content: flex-end; align-items: center; gap: 8px;
    color: var(--leaf); font-size: 14px; line-height: 24px;
  }
  .contacts svg { width: 12px; height: 12px; flex: none; }

  .card--back .brand {
    left: 0; right: 0; top: 62px; justify-content: center;
  }
  .card--back .brand__dot { width: 58px; height: 58px; }
  .card--back .brand__name { font-size: 54px; }

  .pitch {
    position: absolute; left: 0; right: 0; top: 178px; text-align: center;
    color: var(--ink); font-size: 15px; line-height: 21px;
  }
  .pitch__web { color: var(--white); font-size: 14px; margin-top: 10px; }
</style>
</head>
<body>
<main class="canvas">

  <section class="card card--front" aria-label="Business card front">
    <svg class="wave" viewBox="0 0 540 308" preserveAspectRatio="none" aria-hidden="true">
      <path d="M0,308 L0,292 C150,292 250,220 340,140 C395,92 460,84 540,84 L540,308 Z" fill="var(--ink)"/>
      <path d="M60,300 C190,286 270,214 350,140 C400,96 460,90 540,92" fill="none" stroke="var(--sky)" stroke-width="3"/>
    </svg>

    <div class="brand">
      <span class="brand__dot"></span>
      <span class="brand__name">Bright Comb</span>
    </div>

    <div class="identity">
      <p class="identity__name">Maren Holt</p>
      <p class="identity__role">Owner</p>
      <p class="identity__service">All Natural In-Home Lice Removal Services</p>
    </div>

    <ul class="contacts">
      <li>1-855-555-NITS (6487)
        <svg viewBox="0 0 12 12" aria-hidden="true"><path d="M2.5 1 L4.5 1 L5 4 L3.8 5 C4.5 6.6 5.4 7.5 7 8.2 L8 7 L11 7.5 L11 9.5 C11 10.4 10.4 11 9.5 11 C5 11 1 7 1 2.5 C1 1.6 1.6 1 2.5 1 Z" fill="var(--white)"/></svg>
      </li>
      <li>Maren@BrightComb.com
        <svg viewBox="0 0 12 12" aria-hidden="true"><rect x="1" y="2.5" width="10" height="7" rx="1" fill="none" stroke="var(--white)" stroke-width="1.2"/><path d="M1.5 3 L6 6.5 L10.5 3" fill="none" stroke="var(--white)" stroke-width="1.2"/></svg>
      </li>
      <li>www.BrightComb.com
        <svg viewBox="0 0 12 12" aria-hidden="true"><circle cx="6" cy="6" r="5" fill="none" stroke="var(--white)" stroke-width="1.1"/><path d="M1 6 H11 M6 1 C3.5 3.5 3.5 8.5 6 11 M6 1 C8.5 3.5 8.5 8.5 6 11" fill="none" stroke="var(--white)" stroke-width="1"/></svg>
      </li>
    </ul>
  </section>

  <section class="card card--back" aria-label="Business card back">
    <div class="brand">
      <span class="brand__dot"></span>
      <span class="brand__name">Bright Comb</span>
    </div>
    <div class="pitch">
      <p>Try Bright Comb Today and Be Lice Free Tomorrow!</p>
      <p>All Natural In-Home Lice Removal Services</p>
      <p class="pitch__web">www.BrightComb.com</p>
    </div>
  </section>

</main>
</body>
</html>
```